Vestrina KTA - excellent fasteners for automotive industries

We need an A4 ADV page for a Fasteners Magazine - Torque and Tether.
Vestrina is an Italian company founded in 1926. Its name is from the inventor of the Hexagon Socket Head Bolt with Spiral Shank.
We are a leader in fasteners' production all over the world. We produce critical fasteners for automotive engines and more. Our customers are the most important automotive manufacturers.
Our values are: Zero Defects - Total Quality - 100% Made in Italy
Our constant focus since 1926 on meeting the continuous and ever changing market demands has pushed us to constantly dedicate ourselves to research and technological development, enabling us to become a reference point for our Customers.

we want to communicate excellence, research, expertise, modernity
We are ready for the electric transition and have been working for several years on excellent products for the electric motor market

A concept that we want to say is: whether combustion or electric engine Vestrina will be there.

Some our slogan:
spirit of excellence
We are shaping the future

DIMENSION OF THE GRAPHIC
210mm x 297mm plus 3 mm full bleed
190mm x 277mm - safe visible area
4 colors minimum resolution 300 dpi - no spot colors

Automotive industries, screws manufacturing

• we want to communicate excellence, research, expertise, modernity

```html
<!DOCTYPE html>
<html lang="en">
<head>
<meta charset="utf-8">
<title>Vestrina KTA – Spirit of Excellence</title>
<link rel="stylesheet" href="https://fonts.googleapis.com/css2?family=Roboto:wght@400;500;700&family=Roboto+Condensed:wght@500;700&display=swap">
<style>
  :root {
    --backdrop: #f1f1f1;
    --bronze: #8a5f23;
    --bronze-deep: #7d5520;
    --ink-brown: #3a290d;
    --band-dark: #3c2a0f;
    --gold: #d3a135;
    --gold-soft: #c9a04a;
    --navy: #2b2e6c;
    --white: #ffffff;
    --paper: #ffffff;
    --steel: #b9c0c8;
  }
  * { margin: 0; padding: 0; box-sizing: border-box; }
  html, body {
    width: 1200px;
    height: 2456px;
    overflow: hidden;
    background: var(--backdrop);
  }
  .ad-page {
    position: absolute;
    left: 200px;
    top: 662px;
    width: 800px;
    height: 1131px;
    background: var(--paper);
    overflow: hidden;
    font-family: "Roboto", Arial, sans-serif;
    box-shadow: 0 10px 30px rgba(0,0,0,0.18);
  }
  .hero-field {
    position: absolute;
    left: 0; top: 0;
    width: 800px; height: 528px;
    background: linear-gradient(180deg, var(--bronze) 0%, var(--bronze-deep) 100%);
  }
  .kicker {
    position: absolute;
    top: 54px; left: 0; width: 800px;
    text-align: center;
    color: var(--white);
    font-weight: 500;
    font-size: 42px;
    letter-spacing: 20px;
    padding-left: 20px;
  }
  .headline {
    position: absolute;
    top: 88px; left: 0; width: 800px;
    text-align: center;
    color: var(--ink-brown);
    font-weight: 500;
    font-size: 118px;
    line-height: 1;
    letter-spacing: -1px;
  }
  .values-bar {
    position: absolute;
    top: 198px; left: 45px;
    width: 707px; height: 34px;
    background: var(--ink-brown);
    display: flex;
    align-items: center;
    justify-content: center;
    gap: 10px;
    font-family: "Roboto Condensed", Arial, sans-serif;
    font-weight: 500;
    font-size: 19px;
    color: var(--white);
  }
  .values-bar .label { color: var(--gold); }
  .values-bar svg { width: 18px; height: 16px; flex: none; }
  .product-photo {
    position: absolute;
    left: 28px; top: 238px;
    width: 764px; height: 654px;
    background:
      radial-gradient(ellipse at 45% 60%, rgba(205,212,220,0.95) 0%, rgba(185,192,200,0.7) 40%, rgba(255,255,255,0) 72%),
      linear-gradient(180deg, rgba(201,166,60,0.55) 0%, rgba(201,166,60,0.25) 40%, rgba(255,255,255,0) 48%);
  }
  .pillars {
    position: absolute;
    top: 888px; left: 0; width: 800px;
    text-align: center;
    color: var(--navy);
    font-weight: 500;
    font-size: 23px;
    letter-spacing: 3px;
  }
  .pillars-rule {
    position: absolute;
    top: 921px; left: 79px;
    width: 643px; height: 1.5px;
    background: var(--gold-soft);
  }
  .footer-band {
    position: absolute;
    left: 0; top: 949px;
    width: 800px; height: 182px;
    background: var(--band-dark);
  }
  .transition-claim {
    position: absolute;
    left: 63px; top: 40px;
    color: var(--gold);
    font-size: 18px;
    line-height: 22px;
    text-transform: uppercase;
  }
  .transition-note {
    position: absolute;
    left: 63px; top: 96px;
    width: 290px;
    color: var(--white);
    font-size: 12px;
    line-height: 14px;
  }
  .brand-mark {
    position: absolute;
    right: 48px; top: 36px;
    display: flex;
    align-items: center;
    gap: 14px;
    color: var(--gold);
    font-weight: 700;
    font-size: 40px;
    letter-spacing: 0.5px;
  }
  .brand-mark .dot {
    width: 16px; height: 16px;
    border-radius: 50%;
    background: var(--gold);
  }
  .brand-year {
    position: absolute;
    right: 48px; top: 82px;
    color: var(--white);
    font-size: 16px;
    letter-spacing: 2px;
  }
  .contact-line {
    position: absolute;
    right: 48px; top: 108px;
    display: flex;
    align-items: center;
    color: var(--white);
    font-size: 14px;
  }
  .contact-line span + span {
    border-left: 1px solid var(--white);
    margin-left: 9px;
    padding-left: 9px;
  }
</style>
</head>
<body>
  <main class="ad-page">
    <div class="hero-field"></div>

    <div class="product-photo" role="img" aria-label="Photograph of stacked steel hex nuts and bolts on white, with golden nuts faded into the bronze background"></div>

    <p class="kicker">SPIRIT OF</p>
    <h1 class="headline">EXCELLENCE</h1>

    <div class="values-bar">
      <span class="label">OUR VALUES</span>
      <svg viewBox="0 0 18 16"><path d="M2 8.5 L7 13 L16 3" fill="none" stroke="#d3a135" stroke-width="3"/></svg>
      <span>ZERO DEFECTS</span>
      <svg viewBox="0 0 18 16"><path d="M2 8.5 L7 13 L16 3" fill="none" stroke="#d3a135" stroke-width="3"/></svg>
      <span>TOTAL QUALITY</span>
      <svg viewBox="0 0 18 16"><path d="M2 8.5 L7 13 L16 3" fill="none" stroke="#d3a135" stroke-width="3"/></svg>
      <span>100% MADE IN ITALY</span>
    </div>

    <p class="pillars">EXCELLENCE | RESEARCH | EXPERTISE | MODERNITY</p>
    <div class="pillars-rule"></div>

    <footer class="footer-band">
      <p class="transition-claim">Combustion or electric<br>engine Vestrina will be there.</p>
      <p class="transition-note">We are working to get the carbon neutrality in 2035 and -70% CO2 emission in 2030 with a lot of action in the company</p>

      <div class="brand-mark"><span>VESTRINA KTA</span><span class="dot"></span></div>
      <p class="brand-year">SINCE 1926</p>

      <p class="contact-line">
        <span>39 010 555 12</span>
        <span>info@vestrina.com</span>
        <span>www.vestrina.com</span>
      </p>
    </footer>
  </main>
</body>
</html>
```